New Corporate Business Card
Front and Back
I am interested and coming...
pardon me sir about my last comment, i think high res jpg is quietly enough for now, i'll submit design as soon as possible. thanks
could you please upload the .eps or .ai logo file? there will be more great design submitted, thank you. best regards
I have seen some requests for the logos to be in AI or EPS format. I am not bothered at this stage of the quality of the finished sample - it is more the design.
NOTE:
The VORLIN Logo MUST remain with the background yellow as this is part of the logo itself.
DO NOT alter the layout of the logo in ratio to its background. ie. VORLIN must always look like #7 not altered like #3.
Brisk Logo only on front of card not on back. Maybe together with a watermark design.
Back of card to detail contact information and products....(other 4 logos)
In Australia we use the word "mobile" not "cell" when referring to mobile phones.
Hope this helps....get designing!
Please upload ai or eps file of your logo.
could you please upload logo in ai or eps format

```html
<!DOCTYPE html>
<html lang="en">
<head>
<meta charset="utf-8">
<title>Brisk Imaging Stationery</title>
<link href="https://fonts.googleapis.com/css2?family=Roboto:wght@400;700;900&display=swap" rel="stylesheet">
<style>
:root{
  --board:#3a2c24;
  --ink:#0f0f10;
  --paper:#ffffff;
  --red:#d3142b;
  --red-dark:#8e0d1c;
  --grey:#d9d9d9;
  --label:#e9e1da;
  --partner:#e6e6e6;
}
*{margin:0;padding:0;box-sizing:border-box}
html,body{width:1200px;height:746px;overflow:hidden;background:var(--board);font-family:"Roboto",Arial,sans-serif}
.board{position:relative;width:1200px;height:746px}
.label{position:absolute;font-size:8px;color:var(--label);letter-spacing:.2px}
.piece{position:absolute;overflow:hidden;box-shadow:0 3px 8px rgba(0,0,0,.45)}
.brand{display:flex;flex-direction:column;align-items:center;gap:5px;color:var(--paper)}
.brand-dot{width:26px;height:26px;border-radius:50%;background:var(--red)}
.brand-name{font-size:14px;font-weight:700;white-space:nowrap}
.brand-region{font-size:5px;letter-spacing:2px;color:var(--grey);margin-top:-3px;white-space:nowrap}

/* letterhead */
.letterhead{left:48px;top:31px;width:401px;height:612px;background:var(--paper)}
.letterhead-band{height:209px;background:var(--ink);display:flex;justify-content:center;padding-top:72px}
.letterhead-footer{position:absolute;left:14px;bottom:14px;color:var(--ink)}
.fine{font-size:5px;line-height:7px;color:#555}
.phone{font-size:15px;font-weight:900;color:var(--ink)}

/* envelope */
.envelope-front{left:480px;top:108px;width:415px;height:269px;background:var(--ink)}
.envelope-front .red-band{height:36px;background:linear-gradient(var(--red),var(--red-dark))}
.envelope-front .brand{position:absolute;left:30px;top:76px}
.stamp{position:absolute;left:367px;top:60px;width:34px;height:43px;border:1px solid #bbb}
.address-window{position:absolute;left:19px;top:151px;width:120px;height:55px;background:var(--paper)}
.envelope-back{left:480px;top:422px;width:415px;height:214px;background:var(--ink)}
.envelope-back .flap{height:39px;background:linear-gradient(#eee,#bdbdbd)}
.envelope-back .phone{position:absolute;right:42px;bottom:6px;color:var(--paper)}
.decor{position:absolute;border-radius:50%;background:var(--red)}

/* business cards */
.card{left:948px;width:185px;height:122px;background:var(--ink)}
.card-front{top:108px}
.card-front .brand{padding-top:8px}
.card-front .brand-dot{width:18px;height:18px}
.card-front .brand-name{font-size:10px}
.card-red{position:absolute;left:0;right:0;top:55px;bottom:0;background:linear-gradient(var(--red),var(--red-dark));text-align:center;color:var(--paper)}
.person{font-size:8px;font-weight:700;margin-top:10px}
.role{font-size:5px;margin-top:2px}
.card-red .phone{color:var(--paper);font-size:12px;position:absolute;left:0;right:0;bottom:20px}
.card-back-one{top:269px}
.card-back-two{top:413px}
.card-back-two .brand{position:absolute;left:0;right:0;top:14px}
.partners{position:absolute;right:8px;bottom:10px;display:flex;gap:9px;align-items:center}
.partner-box{width:30px;height:14px;background:var(--partner)}
.partner-badge{width:20px;height:14px;background:var(--partner);border-radius:2px}
.partner-oval{width:22px;height:14px;background:var(--partner);border-radius:50%}
</style>
</head>
<body>
<main class="board">
  <span class="label" style="left:48px;top:14px">Letter Head</span>
  <section class="piece letterhead">
    <header class="letterhead-band">
      <div class="brand"><span class="brand-dot"></span><span class="brand-name">Brisk Imaging</span><span class="brand-region">SUPPLY GROUP</span></div>
    </header>
    <footer class="letterhead-footer">
      <p class="fine">Brisk Imaging Pty Ltd</p>
      <p class="fine">14 Harbour Road, Sydney</p>
      <p class="phone">Phone</p>
    </footer>
  </section>

  <span class="label" style="left:480px;top:14px">Envelope</span>
  <span class="label" style="left:480px;top:91px">Front</span>
  <section class="piece envelope-front">
    <div class="red-band"></div>
    <div class="brand"><span class="brand-dot"></span><span class="brand-name">Brisk Imaging</span><span class="brand-region">SUPPLY GROUP</span></div>
    <div class="stamp"></div>
    <div class="address-window"></div>
  </section>

  <span class="label" style="left:480px;top:403px">Back</span>
  <section class="piece envelope-back">
    <div class="flap"></div>
    <div class="decor" style="left:-70px;top:90px;width:170px;height:170px"></div>
    <p class="phone">Phone</p>
  </section>

  <span class="label" style="left:948px;top:14px">Business Card</span>
  <span class="label" style="left:948px;top:91px">Front</span>
  <section class="piece card card-front">
    <div class="brand"><span class="brand-dot"></span><span class="brand-name">Brisk Imaging</span></div>
    <div class="card-red">
      <p class="person">Liam Carter</p>
      <p class="role">National Sales &amp; Marketing Manager</p>
      <p class="phone">Phone</p>
    </div>
  </section>

  <span class="label" style="left:948px;top:254px">Back</span>
  <section class="piece card card-back-one">
    <div class="decor" style="left:-40px;top:-10px;width:110px;height:110px"></div>
    <div class="partners">
      <span class="partner-box"></span>
      <span class="partner-badge"></span>
      <span class="partner-oval"></span>
    </div>
  </section>

  <span class="label" style="left:948px;top:398px">Back</span>
  <section class="piece card card-back-two">
    <div class="brand"><span class="brand-dot"></span><span class="brand-name" style="font-size:9px">Brisk Imaging</span></div>
    <div class="partners">
      <span class="partner-box"></span>
      <span class="partner-badge"></span>
      <span class="partner-oval"></span>
    </div>
  </section>
</main>
</body>
</html>
```